Powerpoint and Word Document Template

Our target market are C-suite executives in banks, credit unions, non-bank financial institutions, financial technology companies and in the law firms, private equity firms and the like that are also advising the industry.

design should convey: confidence, trust, expertise, experience, value, advice, relationship focus.

For the stationery design, we will need the .doc format as well.

Industry/Entity Type

Consulting

Font styles to use
Sans Serif

Colors
0356a4
3277b5
85acd3
cedeed
eaf1f7
ffffff

Requirements
Must have
• must use the logo and color scheme included in the attached zip file. must include a powerpoint template with a cover slide, section break slides, slides for images/graphics, slides for side by side content, and slides for regular content.

Note: this should also include designs for word documents like stationary and envelopes based on the same concept.

```html
<!DOCTYPE html>
<html lang="en">
<head>
<meta charset="utf-8">
<title>Norvale Advisory – Presentation Template</title>
<link href="https://fonts.googleapis.com/css2?family=Montserrat:wght@600;700;800&family=Roboto:wght@400;500;700&display=swap" rel="stylesheet">
<style>
  :root{
    --page:#e7ebef;
    --navy:#0b2d68;
    --blue:#0356a4;
    --mid:#3277b5;
    --light:#85acd3;
    --pale:#cedeed;
    --mist:#eaf1f7;
    --white:#ffffff;
    --ink:#1c1f26;
  }
  *{box-sizing:border-box;margin:0;padding:0}
  html,body{width:1200px;height:3745px;overflow:hidden}
  body{background:var(--page);font-family:"Roboto",Arial,sans-serif;color:var(--ink);position:relative}
  .slide{position:absolute;overflow:hidden;background:var(--white)}
  .slide > *{position:absolute}
  .photo{display:block}
  .photo-towers-night{background:linear-gradient(160deg,#1a1424 0%,#3b2a44 35%,#241a2e 60%,#0e0c16 100%)}
  .photo-boardroom{background:linear-gradient(180deg,#5e5c5e 0%,#6d6966 45%,#3e3128 75%,#2a1f18 100%)}
  .photo-skyline{background:linear-gradient(180deg,#f2ede6 0%,#c9b8a1 45%,#6f5b46 75%,#2b2620 100%)}
  .photo-skyward{background:linear-gradient(170deg,#2d3542 0%,#8c9bb0 35%,#dfe6ee 55%,#5d6874 80%,#1f242b 100%)}
  .photo-navy-towers{background:linear-gradient(150deg,#0b2d68 0%,#12397a 45%,#0a2a60 75%,#081f4a 100%)}

  .brand{display:flex;align-items:center;gap:7px;font-family:"Montserrat",Arial,sans-serif;font-weight:600;letter-spacing:.04em;color:var(--white)}
  .brand-square{border:2px solid currentColor;display:block}
  .brand.dark{color:var(--ink)}

  .frame{border:3px solid var(--blue)}
  .frame.soft{border-color:var(--light)}
  .cover-title{font-family:"Montserrat",Arial,sans-serif;font-weight:700;color:var(--white);line-height:1.15;text-transform:uppercase}
  .accent-title{font-family:"Montserrat",Arial,sans-serif;font-weight:800;color:var(--blue);line-height:1.15;text-transform:uppercase}
  .lead{color:var(--mid);text-transform:uppercase}
  .fine{color:var(--light);line-height:1.3}
  .url{font-weight:700;color:var(--ink)}
  .url.light{color:var(--white)}
  .body-copy p{line-height:1.35;margin-bottom:.8em}
</style>
</head>
<body>

<!-- Cover slide -->
<section class="slide cover" style="left:242px;top:192px;width:716px;height:448px">
  <div class="photo photo-towers-night" role="img" aria-label="Office towers lit at night" style="left:0;top:0;width:716px;height:255px"></div>
  <div class="brand" style="left:215px;top:42px;font-size:22px"><span class="brand-square" style="width:26px;height:26px"></span>NORVALE</div>
  <div class="frame" style="left:166px;top:103px;width:385px;height:269px"></div>
  <h1 class="cover-title" style="left:215px;top:150px;font-size:25px">Business<br>Presentation<br>Title</h1>
  <p class="lead" style="left:215px;top:280px;font-size:16px">Explanatory text, if necessary</p>
  <p class="fine" style="left:215px;top:307px;width:285px;font-size:8px">Advisory for banks, credit unions and financial firms. Clear guidance on strategy, risk and growth, built on long client relationships.</p>
  <p class="url" style="left:215px;top:402px;font-size:8px">www.norvaleadvisory.com</p>
</section>

<!-- Split slide -->
<section class="slide split" style="left:129px;top:810px;width:950px;height:634px">
  <div class="photo photo-boardroom" role="img" aria-label="Empty boardroom with glass walls" style="left:0;top:0;width:950px;height:345px"></div>
  <div class="brand" style="left:31px;top:36px;font-size:19px"><span class="brand-square" style="width:24px;height:24px"></span>NORVALE</div>
  <div class="frame" style="left:80px;top:118px;width:345px;height:404px"></div>
  <h2 class="cover-title" style="left:127px;top:238px;font-size:32px">Split slide<br>template</h2>
  <div class="body-copy" style="left:476px;top:383px;width:390px;font-size:15px">
    <p>Lorem ipsum dolor sit amet, consectetur adipiscing elit. Maecenas finibus ante metus, sed ultricies ligula scelerisque ut. Praesent dignissim mattis sem, nec aliquet lacus vestibulum nec.</p>
    <p>Lorem ipsum dolor sit amet, consectetur adipiscing elit. Maecenas finibus ante metus, sed ultricies ligula scelerisque ut.</p>
  </div>
  <p class="url" style="left:80px;top:566px;font-size:12px">www.norvaleadvisory.com</p>
</section>

<!-- Text slide with icons -->
<section class="slide icon-list" style="left:129px;top:1482px;width:473px;height:315px">
  <div style="left:0;top:0;width:115px;height:315px;background:var(--navy)"></div>
  <div style="left:115px;top:0;width:57px;height:315px;background:var(--blue)"></div>
  <div class="brand" style="left:16px;top:19px;font-size:10px;gap:4px"><span class="brand-square" style="width:12px;height:12px;border-width:1.5px"></span>NORVALE</div>
  <div class="frame" style="left:41px;top:47px;width:393px;height:224px;border-width:2px"></div>
  <svg style="left:133px;top:87px" width="20" height="150" viewBox="0 0 20 150" fill="none" stroke="#fff" stroke-width="1.4">
    <rect x="2" y="2" width="6" height="6"/><rect x="2" y="11" width="6" height="6"/><rect x="11" y="11" width="6" height="6"/><path d="M14 2v6M11 5h6"/>
    <circle cx="10" cy="50" r="7"/><path d="M5 45l10 10M15 45L5 55"/>
    <rect x="2" y="87" width="16" height="13"/><path d="M2 93h16M7 87v6M13 87v6"/>
    <rect x="2" y="128" width="16" height="15"/><path d="M2 133h16M6 125v5M14 125v5M10 136v5M7.5 138.5h5"/>
  </svg>
  <div style="left:189px;top:64px;width:235px;font-size:7px;line-height:1.3">
    <p style="font-family:Montserrat,Arial,sans-serif;font-weight:800;color:var(--navy);font-size:9px;margin-bottom:4px">TEXT SLIDE: TITLE</p>
    <p style="color:var(--blue);font-weight:700;font-size:8px">Lorem ipsum dolor sit amet</p>
    <p style="margin-bottom:4px">Strategic counsel for financial leaders, shaped by decades of industry practice and close client work.</p>
    <p style="color:var(--blue);font-weight:700;font-size:8px">Nunc et est ut nisl convallis facilisis non vel risus</p>
    <p style="margin-bottom:4px">Regulatory insight that helps boards weigh risk, plan capital and act with confidence.</p>
    <p style="color:var(--blue);font-weight:700;font-size:8px">Quisque iaculis tortor a justo rutrum sagittis</p>
    <p style="margin-bottom:4px">Growth programmes for lenders and fintech firms seeking new markets and partners.</p>
    <p style="color:var(--blue);font-weight:700;font-size:8px">Sed sollicitudin tempor eleifend</p>
    <p>Ongoing advice that keeps institutions steady through change, with one trusted team beside them.</p>
  </div>
  <p class="url light" style="left:38px;top:281px;font-size:5px">www.norvaleadvisory.com</p>
</section>

<!-- Text slide with photo, dark -->
<section class="slide photo-dark" style="left:608px;top:1482px;width:471px;height:315px;background:var(--navy)">
  <div class="photo photo-skyline" role="img" aria-label="City skyline of tall towers in warm light" style="left:297px;top:0;width:152px;height:315px"></div>
  <div style="left:449px;top:0;width:22px;height:315px;background:var(--blue)"></div>
  <div class="brand" style="left:16px;top:19px;font-size:10px;gap:4px"><span class="brand-square" style="width:12px;height:12px;border-width:1.5px"></span>NORVALE</div>
  <div class="frame" style="left:39px;top:47px;width:233px;height:224px;border-width:2px;border-color:var(--mid)"></div>
  <div style="left:55px;top:82px;width:200px;color:var(--white)">
    <p style="font-family:Montserrat,Arial,sans-serif;font-weight:800;font-size:9px;line-height:1.2;margin-bottom:6px">TEXT SLIDE WITH PHOTO,<br>EXPLANATORY TEXT</p>
    <p style="font-size:6.5px;line-height:1.35">We advise banks, credit unions and fintech firms on strategy, risk and growth. Our partners bring decades of experience to every board discussion.</p>
    <p style="font-size:6.5px;line-height:1.35;margin-top:4px">Each engagement begins with listening and ends with a clear plan. We stay close after delivery so results hold over time.</p>
  </div>
  <p class="url light" style="left:38px;top:281px;font-size:5px">www.norvaleadvisory.com</p>
</section>

<!-- Section slide -->
<section class="slide section-break" style="left:129px;top:1836px;width:950px;height:632px">
  <div class="photo photo-navy-towers" role="img" aria-label="Office tower facade in a deep blue tint" style="left:380px;top:0;width:570px;height:632px"></div>
  <div class="brand dark" style="left:31px;top:36px;font-size:19px"><span class="brand-square" style="width:24px;height:24px"></span>NORVALE</div>
  <div class="frame" style="left:80px;top:118px;width:791px;height:403px"></div>
  <h2 class="accent-title" style="left:127px;top:198px;font-size:35px">Text title<br>of the slide</h2>
  <svg style="left:127px;top:295px" width="78" height="78" viewBox="0 0 78 78">
    <circle cx="39" cy="39" r="39" fill="#3277b5"/>
    <g fill="none" stroke="#fff" stroke-width="2.4"><rect x="25" y="40" width="8" height="12"/><rect x="34" y="33" width="8" height="19"/><rect x="43" y="26" width="8" height="26"/></g>
  </svg>
  <div style="left:450px;top:198px;width:385px;color:var(--white)">
    <p style="font-family:Montserrat,Arial,sans-serif;font-weight:800;font-size:22px;line-height:1.2;margin-bottom:12px">SLIDE SUBTITLE,<br>EXPLANATORY TEXT</p>
    <div class="body-copy" style="font-size:15px">
      <p>Lorem ipsum dolor sit amet, consectetur adipiscing elit. Maecenas finibus ante metus, sed ultricies ligula scelerisque ut. Praesent dignissim mattis sem, nec aliquet lacus vestibulum nec.</p>
      <p>Lorem ipsum dolor sit amet, consectetur adipiscing elit. Maecenas finibus ante metus, sed ultricies ligula scelerisque ut. Praesent dignissim mattis sem, nec aliquet lacus vestibulum nec.</p>
    </div>
  </div>
  <p class="url" style="left:80px;top:566px;font-size:12px">www.norvaleadvisory.com</p>
</section>

<!-- Text slide with photo, light -->
<section class="slide photo-light" style="left:129px;top:2506px;width:950px;height:633px">
  <div style="left:0;top:0;width:47px;height:633px;background:var(--mid)"></div>
  <div class="photo photo-skyward" role="img" aria-label="Looking up at skyscrapers against a cloudy sky" style="left:47px;top:0;width:305px;height:633px"></div>
  <div class="brand" style="left:31px;top:36px;font-size:19px"><span class="brand-square" style="width:24px;height:24px"></span>NORVALE</div>
  <div class="frame soft" style="left:416px;top:95px;width:472px;height:449px"></div>
  <div style="left:453px;top:165px;width:390px">
    <p class="accent-title" style="font-size:22px;margin-bottom:22px">Text slide with photo,<br>explanatory text</p>
    <div class="body-copy" style="font-size:14.5px">
      <p>Lorem ipsum dolor sit amet, consectetur adipiscing elit. Maecenas finibus ante metus, sed ultricies ligula scelerisque ut. Praesent dignissim mattis sem, nec aliquet lacus vestibulum nec.</p>
      <p>Nunc et est ut nisl convallis facilisis non vel risus. Praesent blandit euismod enim, sit amet vestibulum odio. Vivamus lorem libero, rutrum scelerisque ipsum sed, consectetur laoreet urna.</p>
      <p>Quisque iaculis tortor a justo rutrum sagittis. Praesent quis lacus tempor, finibus augue nec, auctor neque. Suspendisse egestas vulputate nunc, ut ultricies augue luctus non.</p>
    </div>
  </div>
  <p class="url light" style="left:79px;top:566px;font-size:12px">www.norvaleadvisory.com</p>
</section>

<!-- Cover, small -->
<section class="slide cover-small" style="left:129px;top:3219px;width:473px;height:316px">
  <div class="photo photo-towers-night" role="img" aria-label="Office towers lit at night" style="left:0;top:0;width:473px;height:171px"></div>
  <div class="brand" style="left:142px;top:23px;font-size:14px;gap:5px"><span class="brand-square" style="width:16px;height:16px;border-width:1.5px"></span>NORVALE</div>
  <div class="frame" style="left:109px;top:69px;width:256px;height:180px;border-width:2px"></div>
  <h3 class="cover-title" style="left:142px;top:104px;font-size:16px">Business<br>Presentation<br>Title</h3>
  <p class="lead" style="left:142px;top:190px;font-size:10px">Explanatory text, if necessary</p>
  <p class="fine" style="left:142px;top:206px;width:190px;font-size:5.5px">Advisory for banks, credit unions and financial firms. Clear guidance on strategy, risk and growth, built on long client relationships.</p>
  <p class="url" style="left:142px;top:283px;font-size:5px">www.norvaleadvisory.com</p>
</section>

<!-- Split slide, small -->
<section class="slide split-small" style="left:608px;top:3219px;width:471px;height:316px">
  <div class="photo photo-boardroom" role="img" aria-label="Empty boardroom with glass walls" style="left:0;top:144px;width:471px;height:172px"></div>
  <div class="brand dark" style="left:16px;top:17px;font-size:10px;gap:4px"><span class="brand-square" style="width:12px;height:12px;border-width:1.5px"></span>NORVALE</div>
  <div class="frame" style="left:41px;top:58px;width:170px;height:226px;border-width:2px"></div>
  <h3 class="accent-title" style="left:63px;top:77px;font-size:16px;font-weight:700">Split slide<br>template</h3>
  <div style="left:236px;top:58px;width:185px;font-size:6px;line-height:1.3">
    <p style="margin-bottom:5px">Trusted advice for financial leaders, grounded in deep sector knowledge and long relationships.</p>
    <p>Clear plans for strategy, risk and growth, delivered by one experienced team.</p>
  </div>
  <p class="url light" style="left:41px;top:299px;font-size:5px">www.norvaleadvisory.com</p>
</section>

</body>
</html>
```